Anzeigengestaltung für Dienstleister für die professionelle Planung und Beschaffung von IT-Lösungen
Zielgruppe
Wir sind Dienstleister für die professionelle Planung und Beschaffung von IT-Lösungen.
Wir bieten umfassende und umfangreiche sowie produktneutrale Beratung zur Umsetzung Ihrer Digitalisierungsprojekte.
Unser Ziel ist es, Ihre individuellen Wünsche und Anforderungen mit speziell auf Sie abgestimmten Konzepten zu realisieren. Hierbei verstehen wir uns als Teamplayer, der alle Aspekte der verschiedenen Fachbereiche zu kombinieren versteht.
Fokus:
Neben den technischen Lösungen erarbeiten wir die detaillierten Anforderungen für Vergabeverfahren (öffentliche Ausschreibung national und EU weit)
Beratung
Planung
Erarbeiten von professionellen und produktneutralen Ausschreibungsunterlagen
Durchführen der Ausschreibung und Vergabe
Professionelle Dokumentation
Professionelle Projektbegleitung bis zur Abnahme und Abrechnung
Bereiche:
Digitalisierung Schulen
Rechenzentren
Telefon Lösungen
Druck Lösungen
Netzwerk und WLAN Lösungen
Zielkunden:
Öffentliche Kunde wie z.B. Kommunen, Schulen, Rathäuser, Hochschulen
Aufgabenstellung
OnePager A4 als Werbeflyer zur Darstellung meines Unternehmen, Neukundengewinnung

```html
<!DOCTYPE html>
<html lang="de">
<head>
<meta charset="utf-8">
<title>NetzKonzept – Flyer</title>
<link href="https://fonts.googleapis.com/css2?family=Montserrat:ital,wght@0,400;0,500;0,700;1,500&display=swap" rel="stylesheet">
<style>
  :root {
    --green: #a5c614;
    --blue: #4a95bc;
    --text: #333;
    --paper: #fff;
    --stage: #d5d6d8;
  }
  * { box-sizing: border-box; margin: 0; padding: 0; }
  html, body { width: 1200px; height: 840px; overflow: hidden; }
  body {
    background: var(--stage);
    font-family: "Montserrat", sans-serif;
    color: var(--text);
    position: relative;
  }
  .flyer {
    position: absolute;
    top: 60px;
    width: 505px;
    height: 720px;
    background: var(--paper);
    overflow: hidden;
  }
  .flyer--green { left: 65px; --band: var(--green); }
  .flyer--blue { left: 630px; --band: var(--blue); }

  .brand {
    position: absolute; left: 46px; top: 48px;
    display: flex; align-items: center; gap: 8px;
    font-size: 24px; font-weight: 400; letter-spacing: 0.5px; color: var(--text);
  }
  .brand__dot { width: 16px; height: 16px; border-radius: 50%; background: var(--green); }

  .tagline {
    position: absolute; left: 265px; top: 66px; width: 230px;
    font-size: 9.8px; line-height: 12.4px; font-style: italic; font-weight: 500;
    color: var(--green);
  }

  .intro {
    position: absolute; left: 30px; top: 141px; width: 200px;
    font-size: 9.6px; line-height: 12.2px;
  }
  .intro p + p { margin-top: 6px; }
  .hl { color: var(--green); font-weight: 700; }

  .connector { position: absolute; height: 1px; background: var(--green); opacity: .7; }
  .connector--intro { left: 210px; top: 146px; width: 42px; }
  .connector--focus { left: 252px; top: 283px; width: 40px; }

  .photo { position: absolute; border: 5px solid var(--green); }
  .photo--team {
    left: 265px; top: 131px; width: 250px; height: 124px;
    border-right: none; border-radius: 14px 0 0 14px;
    background: linear-gradient(135deg, #3d6f98 0%, #8db0c8 45%, #e9e4d6 70%, #f0c23a 100%);
  }
  .photo--tender {
    left: -5px; top: 264px; width: 247px; height: 153px;
    border-left: none; border-radius: 0 14px 14px 0;
    background: linear-gradient(120deg, #e8e3da 0%, #2d6fa4 35%, #1c5383 65%, #dfe3e6 100%);
  }
  .photo--keyboard {
    left: 242px; top: 341px; width: 124px; height: 63px;
    border-left: none; border-radius: 0 12px 12px 0;
    background: linear-gradient(150deg, #dfe8f0 0%, #b8cde0 55%, #e8c7b0 100%);
  }

  .focus {
    position: absolute; left: 285px; top: 274px; width: 190px;
    text-align: right; font-size: 9.6px; line-height: 12.2px;
  }

  .section-title {
    position: absolute; color: var(--green); font-weight: 700;
    font-size: 12.6px; line-height: 15.4px;
  }
  .section-title--services { left: 21px; top: 437px; }
  .section-title--areas { left: 297px; top: 454px; }

  .list { position: absolute; list-style: none; font-size: 9.8px; line-height: 12.2px; }
  .list li { position: absolute; left: 0; display: flex; gap: 7px; white-space: nowrap; }
  .list svg { flex: none; width: 11px; height: 11px; margin-top: 0; }
  .list--services { left: 21px; top: 483px; width: 260px; }
  .list--areas { left: 300px; top: 483px; width: 190px; }

  .footer {
    position: absolute; left: 0; right: 0; top: 675px; height: 33px;
    background: var(--band); color: #fff; text-align: center;
    font-size: 9.6px; line-height: 12.2px; padding-top: 4px;
  }
  .footer strong { font-weight: 700; }
</style>
</head>
<body>

<!-- Variante Grün -->
<article class="flyer flyer--green">
  <div class="brand"><span class="brand__dot"></span>NETZKONZEPT</div>
  <p class="tagline">Dienstleister für die professionelle Planung<br>und Beschaffung von IT-Lösungen.</p>

  <div class="intro">
    <p><span class="hl">Unser Ziel</span> ist es, Ihre individuellen Wünsche und Anforderungen mit speziell auf Sie abgestimmten Konzepten zu realisieren.</p>
    <p>Hierbei verstehen wir uns als Team-player, der alle Aspekte der verschie-denen Fachbereiche zu kombinieren versteht.</p>
  </div>
  <span class="connector connector--intro"></span>
  <div class="photo photo--team" role="img" aria-label="Foto: Team beugt sich über Baupläne mit digitalen Symbolen"></div>

  <div class="photo photo--tender" role="img" aria-label="Foto: Laptop mit Paragrafenzeichen und Schriftzug Vergabeverfahren"></div>
  <div class="photo photo--keyboard" role="img" aria-label="Foto: Tastatur mit Taste Ausschreibung"></div>
  <span class="connector connector--focus"></span>
  <p class="focus">Neben den technischen Lösungen erarbeiten wir <span class="hl">die detaillierten An-forderungen für Vergabeverfahren</span> (öffentliche Ausschreibung national und EU weit).</p>

  <h2 class="section-title section-title--services">Unser Leistungsspektrum<br>der IT Projektplanung:</h2>
  <ul class="list list--services">
    <li style="top:0"><svg viewBox="0 0 12 12"><rect x=".6" y="1.6" width="9.5" height="9.5" fill="none" stroke="#a5c614" stroke-width="1.2"/><path d="M3 6l2.3 2.4L11.4.8" fill="none" stroke="#a5c614" stroke-width="1.6"/></svg>Beratung</li>
    <li style="top:22px"><svg viewBox="0 0 12 12"><rect x=".6" y="1.6" width="9.5" height="9.5" fill="none" stroke="#a5c614" stroke-width="1.2"/><path d="M3 6l2.3 2.4L11.4.8" fill="none" stroke="#a5c614" stroke-width="1.6"/></svg>Planung</li>
    <li style="top:44px"><svg viewBox="0 0 12 12"><rect x=".6" y="1.6" width="9.5" height="9.5" fill="none" stroke="#a5c614" stroke-width="1.2"/><path d="M3 6l2.3 2.4L11.4.8" fill="none" stroke="#a5c614" stroke-width="1.6"/></svg><span>Erarbeiten von professionellen<br>und produktneutralen Aus-<br>schreibungsunterlagen</span></li>
    <li style="top:91px"><svg viewBox="0 0 12 12"><rect x=".6" y="1.6" width="9.5" height="9.5" fill="none" stroke="#a5c614" stroke-width="1.2"/><path d="M3 6l2.3 2.4L11.4.8" fill="none" stroke="#a5c614" stroke-width="1.6"/></svg><span>Durchführen der Ausschrei-<br>bung und Vergabe</span></li>
    <li style="top:125px"><svg viewBox="0 0 12 12"><rect x=".6" y="1.6" width="9.5" height="9.5" fill="none" stroke="#a5c614" stroke-width="1.2"/><path d="M3 6l2.3 2.4L11.4.8" fill="none" stroke="#a5c614" stroke-width="1.6"/></svg>Professionelle Dokumentation</li>
    <li style="top:147px"><svg viewBox="0 0 12 12"><rect x=".6" y="1.6" width="9.5" height="9.5" fill="none" stroke="#a5c614" stroke-width="1.2"/><path d="M3 6l2.3 2.4L11.4.8" fill="none" stroke="#a5c614" stroke-width="1.6"/></svg><span>Professionelle Projektbeglei-<br>tung bis zur Abnahme und<br>Abrechnung</span></li>
  </ul>

  <h2 class="section-title section-title--areas">Bereiche:</h2>
  <ul class="list list--areas">
    <li style="top:0"><svg viewBox="0 0 12 12"><path d="M6 1a5 5 0 1 0 5 5" fill="none" stroke="#a5c614" stroke-width="1.8"/><path d="M3 6h6M6.5 3.5L9 6 6.5 8.5" fill="none" stroke="#a5c614" stroke-width="1.6"/></svg>Digitalisierung Schulen</li>
    <li style="top:27px"><svg viewBox="0 0 12 12"><path d="M6 1a5 5 0 1 0 5 5" fill="none" stroke="#a5c614" stroke-width="1.8"/><path d="M3 6h6M6.5 3.5L9 6 6.5 8.5" fill="none" stroke="#a5c614" stroke-width="1.6"/></svg>Rechenzentren</li>
    <li style="top:54px"><svg viewBox="0 0 12 12"><path d="M6 1a5 5 0 1 0 5 5" fill="none" stroke="#a5c614" stroke-width="1.8"/><path d="M3 6h6M6.5 3.5L9 6 6.5 8.5" fill="none" stroke="#a5c614" stroke-width="1.6"/></svg>Telefon-Lösungen</li>
    <li style="top:81px"><svg viewBox="0 0 12 12"><path d="M6 1a5 5 0 1 0 5 5" fill="none" stroke="#a5c614" stroke-width="1.8"/><path d="M3 6h6M6.5 3.5L9 6 6.5 8.5" fill="none" stroke="#a5c614" stroke-width="1.6"/></svg>Druck-Lösungen</li>
    <li style="top:108px"><svg viewBox="0 0 12 12"><path d="M6 1a5 5 0 1 0 5 5" fill="none" stroke="#a5c614" stroke-width="1.8"/><path d="M3 6h6M6.5 3.5L9 6 6.5 8.5" fill="none" stroke="#a5c614" stroke-width="1.6"/></svg><span>Netzwerk- und<br>WLAN-Lösungen</span></li>
  </ul>

  <footer class="footer">
    <strong>NetzKonzept GmbH</strong> · Lindenallee 14 · 88400 Musterfeld<br>
    Tel: 07500 / 1 23 45-0 · E-Mail: info@netzkonzept-beispiel.de · www.netzkonzept-beispiel.de
  </footer>
</article>

<!-- Variante Blau -->
<article class="flyer flyer--blue">
  <div class="brand"><span class="brand__dot"></span>NETZKONZEPT</div>
  <p class="tagline">Dienstleister für die professionelle Planung<br>und Beschaffung von IT-Lösungen.</p>

  <div class="intro">
    <p><span class="hl">Unser Ziel</span> ist es, Ihre individuellen Wünsche und Anforderungen mit speziell auf Sie abgestimmten Konzepten zu realisieren.</p>
    <p>Hierbei verstehen wir uns als Team-player, der alle Aspekte der verschie-denen Fachbereiche zu kombinieren versteht.</p>
  </div>
  <span class="connector connector--intro"></span>
  <div class="photo photo--team" role="img" aria-label="Foto: Team beugt sich über Baupläne mit digitalen Symbolen"></div>

  <div class="photo photo--tender" role="img" aria-label="Foto: Laptop mit Paragrafenzeichen und Schriftzug Vergabeverfahren"></div>
  <div class="photo photo--keyboard" role="img" aria-label="Foto: Tastatur mit Taste Ausschreibung"></div>
  <span class="connector connector--focus"></span>
  <p class="focus">Neben den technischen Lösungen erarbeiten wir <span class="hl">die detaillierten An-forderungen für Vergabeverfahren</span> (öffentliche Ausschreibung national und EU weit).</p>

  <h2 class="section-title section-title--services">Unser Leistungsspektrum<br>der IT Projektplanung:</h2>
  <ul class="list list--services">
    <li style="top:0"><svg viewBox="0 0 12 12"><rect x=".6" y="1.6" width="9.5" height="9.5" fill="none" stroke="#a5c614" stroke-width="1.2"/><path d="M3 6l2.3 2.4L11.4.8" fill="none" stroke="#a5c614" stroke-width="1.6"/></svg>Beratung</li>
    <li style="top:22px"><svg viewBox="0 0 12 12"><rect x=".6" y="1.6" width="9.5" height="9.5" fill="none" stroke="#a5c614" stroke-width="1.2"/><path d="M3 6l2.3 2.4L11.4.8" fill="none" stroke="#a5c614" stroke-width="1.6"/></svg>Planung</li>
    <li style="top:44px"><svg viewBox="0 0 12 12"><rect x=".6" y="1.6" width="9.5" height="9.5" fill="none" stroke="#a5c614" stroke-width="1.2"/><path d="M3 6l2.3 2.4L11.4.8" fill="none" stroke="#a5c614" stroke-width="1.6"/></svg><span>Erarbeiten von professionellen<br>und produktneutralen Aus-<br>schreibungsunterlagen</span></li>
    <li style="top:91px"><svg viewBox="0 0 12 12"><rect x=".6" y="1.6" width="9.5" height="9.5" fill="none" stroke="#a5c614" stroke-width="1.2"/><path d="M3 6l2.3 2.4L11.4.8" fill="none" stroke="#a5c614" stroke-width="1.6"/></svg><span>Durchführen der Ausschrei-<br>bung und Vergabe</span></li>
    <li style="top:125px"><svg viewBox="0 0 12 12"><rect x=".6" y="1.6" width="9.5" height="9.5" fill="none" stroke="#a5c614" stroke-width="1.2"/><path d="M3 6l2.3 2.4L11.4.8" fill="none" stroke="#a5c614" stroke-width="1.6"/></svg>Professionelle Dokumentation</li>
    <li style="top:147px"><svg viewBox="0 0 12 12"><rect x=".6" y="1.6" width="9.5" height="9.5" fill="none" stroke="#a5c614" stroke-width="1.2"/><path d="M3 6l2.3 2.4L11.4.8" fill="none" stroke="#a5c614" stroke-width="1.6"/></svg><span>Professionelle Projektbeglei-<br>tung bis zur Abnahme und<br>Abrechnung</span></li>
  </ul>

  <h2 class="section-title section-title--areas">Bereiche:</h2>
  <ul class="list list--areas">
    <li style="top:0"><svg viewBox="0 0 12 12"><path d="M6 1a5 5 0 1 0 5 5" fill="none" stroke="#a5c614" stroke-width="1.8"/><path d="M3 6h6M6.5 3.5L9 6 6.5 8.5" fill="none" stroke="#a5c614" stroke-width="1.6"/></svg>Digitalisierung Schulen</li>
    <li style="top:27px"><svg viewBox="0 0 12 12"><path d="M6 1a5 5 0 1 0 5 5" fill="none" stroke="#a5c614" stroke-width="1.8"/><path d="M3 6h6M6.5 3.5L9 6 6.5 8.5" fill="none" stroke="#a5c614" stroke-width="1.6"/></svg>Rechenzentren</li>
    <li style="top:54px"><svg viewBox="0 0 12 12"><path d="M6 1a5 5 0 1 0 5 5" fill="none" stroke="#a5c614" stroke-width="1.8"/><path d="M3 6h6M6.5 3.5L9 6 6.5 8.5" fill="none" stroke="#a5c614" stroke-width="1.6"/></svg>Telefon-Lösungen</li>
    <li style="top:81px"><svg viewBox="0 0 12 12"><path d="M6 1a5 5 0 1 0 5 5" fill="none" stroke="#a5c614" stroke-width="1.8"/><path d="M3 6h6M6.5 3.5L9 6 6.5 8.5" fill="none" stroke="#a5c614" stroke-width="1.6"/></svg>Druck-Lösungen</li>
    <li style="top:108px"><svg viewBox="0 0 12 12"><path d="M6 1a5 5 0 1 0 5 5" fill="none" stroke="#a5c614" stroke-width="1.8"/><path d="M3 6h6M6.5 3.5L9 6 6.5 8.5" fill="none" stroke="#a5c614" stroke-width="1.6"/></svg><span>Netzwerk- und<br>WLAN-Lösungen</span></li>
  </ul>

  <footer class="footer">
    <strong>NetzKonzept GmbH</strong> · Lindenallee 14 · 88400 Musterfeld<br>
    Tel: 07500 / 1 23 45-0 · E-Mail: info@netzkonzept-beispiel.de · www.netzkonzept-beispiel.de
  </footer>
</article>

</body>
</html>
```